VeloRoot Sample Packaging Design

We need a design - with assistance on logo and colours - of a box containing sample sachets of a new natural sports supplement for endurance athletes.
We have an idea of logo and colours but would like input, ideas and assistance to create a cool new brand.

The product is based on natural beetroot powder which is scientifically backed to improve sports performance.
We like clean minimal branding that looks scientific - such as Qvx Dietics, Heap Grains, Brain Den Max and TuK Gamma Burn sachets.

Attached is the type of package we will be using with matt black sachets, so clean white with potentially a beetroot colour (hex 691a40??) and grey (a3b2c2??) but we would like your professional and creative input.

I have attached a rough logo mock up of the logo I designed, happy for you to develop this by making it a bit cleaner (left edges angled or curved maybe- change font also maybe??) or your own ideas if clean, simple and effective. I based mine off the Swift Arrow logo and PB works well with VeloRoot and Personal Best.

The final design should be clean, minimalist, high end sports supplement with a science and natural beetroot feel.
Box size: 300mm x 130mm x 14mm

Target Market(s)

Elite athletes and professionals wanting natural and science-backed supplements that work. Probably mainly men.
The customers are long distance sportspeople and NOT bodybuilders! Including triathletes, cyclists, long distance runners and swimmers.
The brand must also appeal to club level athletes and weekend warriors (but this should be easy if it's targeted at elite level first)

Industry/Entity Type

Supplement

Font styles to use
Sans Serif

Colors

Designer to choose colors to be used in the design.

Requirements
Must have
• - New logo (I like the Swift Arrow logo but open to new ideas!)
• - Clean, scientific look with a twist of "I'm natural and not full of sports supplement junk!!"
• - A shade of beetroot red/purple as the signature colour, without looking too feminine.
• - Our slogan is "Beat your best"
Should not have
• A bodybuilder look.

```html
<!DOCTYPE html>
<html lang="en">
<head>
<meta charset="utf-8">
<title>VeloRoot Sample Box – Lid</title>
<link rel="stylesheet" href="https://fonts.googleapis.com/css2?family=Open+Sans:wght@400;600;700&display=swap">
<style>
  :root {
    --beetroot: #7a0033;
    --beetroot-deep: #690029;
    --lid-white: #ffffff;
    --backdrop: #f2f2f2;
    --shadow: rgba(0, 0, 0, 0.12);
  }
  html, body {
    margin: 0;
    padding: 0;
    width: 1200px;
    height: 907px;
    overflow: hidden;
    background: var(--backdrop);
    font-family: "Open Sans", Arial, sans-serif;
  }
  .canvas {
    position: relative;
    width: 1200px;
    height: 907px;
  }
  .box-lid {
    position: absolute;
    left: 100px;
    top: 236px;
    width: 1000px;
    height: 434px;
    box-shadow: 0 12px 30px var(--shadow);
  }
  .box-lid svg {
    display: block;
    width: 100%;
    height: 100%;
  }
  .lid-beetroot { fill: var(--beetroot); }
  .lid-white { fill: var(--lid-white); }
  .curve-rule {
    fill: none;
    stroke: var(--lid-white);
    stroke-width: 3;
  }
  .tagline {
    fill: var(--beetroot);
    font-size: 36px;
    font-weight: 400;
    letter-spacing: 0.5px;
  }
  .brand-name {
    fill: var(--lid-white);
    font-size: 48px;
    font-weight: 700;
  }
  .brand-square { fill: var(--lid-white); }
  .product-copy {
    fill: var(--lid-white);
    font-size: 12.5px;
    font-weight: 400;
  }
</style>
</head>
<body>
<main class="canvas">
  <section class="box-lid" aria-label="VeloRoot sample box lid">
    <svg viewBox="0 0 1000 434" xmlns="http://www.w3.org/2000/svg">
      <rect class="lid-beetroot" x="0" y="0" width="1000" height="434"/>
      <path class="lid-white" d="M0 0 H1000 V320 C600 360 250 250 0 30 Z"/>
      <path class="curve-rule" d="M0 44 C250 264 600 374 1000 334"/>

      <text class="tagline" x="470" y="150" text-anchor="middle">Beat your best</text>

      <rect class="brand-square" x="60" y="268" width="38" height="38"/>
      <text class="brand-name" x="112" y="305" textLength="260" lengthAdjust="spacingAndGlyphs">VELOROOT</text>

      <text class="product-copy" x="60" y="358">Each sachet holds pure beetroot powder, tested for purity and blended for steady endurance on long days.</text>
      <text class="product-copy" x="60" y="380">Mix one sachet with water two hours before training or racing, and take daily through your build phase.</text>
      <text class="product-copy" x="60" y="402">No added sugar, no fillers, no artificial colours. Store dry and cool, away from direct sunlight.</text>
    </svg>
  </section>
</main>
</body>
</html>
```